Sympathy Gift Supplier needs packaging designs

We provide sympathy/bereavement gifts such as memorial candles and picture frames for those who recently lost a loved one. We need packaging design for our boxes that will be uplifting and positive, yet elegant.

We have attached our logo in white and black as well as a saying we would like on the box, and what we need on the back panel.
Ignore the black as it was something we were working on for another product.

These products will be given as gifts to people who lost a loved one as remembrance.

• Back panel details (provided)
Memorial quote (provided)
Must be appropriate for this type of product

```html
<!DOCTYPE html>
<html lang="en">
<head>
<meta charset="utf-8">
<title>Memorial Candle Packaging Panels</title>
<link href="https://fonts.googleapis.com/css2?family=Quicksand:wght@400;500&family=Sacramento&display=swap" rel="stylesheet">
<style>
  :root {
    --backdrop: #b0afb0;
    --panel: #f7f7f7;
    --panel-shade: #ececec;
    --ink: #1f1f1f;
    --script-ink: #6a6a6a;
    --gold-light: #f3e3c4;
    --gold: #e2c08a;
  }
  * { margin: 0; padding: 0; box-sizing: border-box; }
  html, body { width: 1200px; height: 960px; overflow: hidden; }
  body {
    background: var(--backdrop);
    position: relative;
    font-family: "Quicksand", sans-serif;
    color: var(--ink);
  }
  .panel {
    position: absolute;
    background: radial-gradient(ellipse at 40% 35%, #fbfbfb 0%, var(--panel) 55%, var(--panel-shade) 100%);
  }
  .panel--front { left: 59px; top: 224px; width: 512px; height: 512px; }
  .panel--back  { left: 624px; top: 224px; width: 517px; height: 517px; }

  .floral-art {
    position: absolute;
    left: 117px; top: 48px;
    width: 280px; height: 284px;
    border-radius: 8px;
    background: radial-gradient(circle at 50% 45%, #ffffff 0%, var(--gold-light) 55%, rgba(226,192,138,0.35) 100%);
  }
  .memorial-quote {
    position: absolute;
    left: 0; right: 0; top: 364px;
    text-align: center;
    font-family: "Sacramento", cursive;
    font-size: 26px;
    line-height: 28px;
    color: var(--script-ink);
  }

  .back-copy {
    position: absolute;
    left: 0; right: 0; top: 58px;
    text-align: center;
  }
  .back-copy__heading {
    font-size: 14px;
    font-weight: 500;
    letter-spacing: 3px;
    line-height: 20px;
  }
  .back-copy__warnings {
    margin-top: 6px;
    font-size: 14.5px;
    line-height: 25.6px;
  }
  .back-copy__heading--instructions { margin-top: 24px; }
  .back-copy__instructions {
    width: 400px;
    margin: 6px auto 0;
    font-size: 14.5px;
    line-height: 26px;
  }
  .brand-mark {
    position: absolute;
    left: 0; right: 0; top: 432px;
    display: flex; align-items: center; justify-content: center; gap: 8px;
    font-size: 17px;
    font-weight: 500;
    color: var(--ink);
  }
  .brand-mark__dot {
    width: 12px; height: 12px; border-radius: 50%;
    background: var(--gold);
  }
</style>
</head>
<body>
  <section class="panel panel--front">
    <div class="floral-art" role="img" aria-label="Fine gold line drawing of peonies and blossoms over a thin diamond frame"></div>
    <p class="memorial-quote">
      When the people we love are taken from us<br>
      the way to have them live on is to<br>
      never stop loving them...
    </p>
  </section>

  <section class="panel panel--back">
    <div class="back-copy">
      <h2 class="back-copy__heading">WARNING</h2>
      <p class="back-copy__warnings">
        Burn within sight.<br>
        Keep away from flammable objects.<br>
        Keep away from children and pets.
      </p>
      <h2 class="back-copy__heading back-copy__heading--instructions">BURNING INSTRUCTIONS</h2>
      <p class="back-copy__instructions">
        Trim wick to 1/4″ before lighting. Keep candle from materials including matches and wick trimmings. Only burn the candle on a level fire resistant surface. Do not burn candle for more than four (4) hours at a time. Stop use when only 1/4″ of wax remains.
      </p>
    </div>
    <div class="brand-mark">
      <span class="brand-mark__dot"></span>
      <span class="brand-mark__name">Serene Grove</span>
    </div>
  </section>
</body>
</html>
```